Bright and beautiful business card for a coach

I'm a personal and business coach based in Perth, Australia. I need a business card that whilst subtle and elegant, will stand out and appeal on a table full of cards.

My business name is Tide Mentoring and the business card must represent the warmth and brightness implied in the name, without being gimmicky. It must have a warmth and appeal and be easy to read.

I prefer clean, minimalist designs.

It must align with the feel of my website and socials: https://www.tidementoring.com.au/
https://www.instagram.com/tidementoringau/
https://www.facebook.com/tidementoringau
Updates

Hi Designers Thank you so much for taking the time to submit designs. I wonder if I could have explained myself a little better. Most of the designs that have been submitted look rather formal and many have quite corporate looking embellishments on them (to my eye). I would like softer, warmer, more organic. I’m open to people playing about and being more abstract, using softer embellishments (e.g the line drawing flowers and grasses I’ve used in my socials) incorporating other colours from my palette or like the social icons in my email signature (in PDF), perhaps playing with size/oversize, playing with the bleed. Please don’t be constrained by what I’ve already done, it merely needs to compliment. I’m sorry if I’m not using the right words or have led you astray. I’m no designer, but I’ve done my website, socials, email signature etc all myself (my logo was a design contest) and I was really hoping for my business card to be something more creative than I could have made with a template. Reminder: No black cards/sides please. Thank you 😊

Target Market(s)

Individuals, most likely but not all female. Creative thinkers. Likely professionals.

Industry/Entity Type

Business & Personal Coach

Contact Information for Business Card

(Tide Mentoring Logo) Name: Maren Delsby; Title: Business & Personal Coach; Phone number: +61 (0)438 915307; Email: maren@tidementoring.com.au; Website: https://tidementoring.com.au; Social icons for Facebook, Instagram & LinkedIn: @tidementoringAU. Optional strapline: "A thinking partner to help you cut through the noise"

Font styles to use
Sans Serif

Colors
00AB8E
00BBA5
67D7C9
C6EFE9
E9F9F6
59FF00
82FF00
B8FF75
E3FFCB
F4FFEA
FFC000
F8CF3A
FAE287
FDF2CF
FEFAEE

Requirements
Must have
• Must align with feel of my website and socials. Must have a pop of #FFC000 (possibly whole of one side, or at least a block). Bright or white background. Easy to read.
Nice to have
• Possibly incorporate the sunshine/grass picture I have used in website and socials - will upload.
Should not have
• Must not be black or dark. Not impersonal or corporate looking.

```html
<!DOCTYPE html>
<html lang="en">
<head>
<meta charset="utf-8">
<title>Tide Mentoring – Business Card</title>
<link href="https://fonts.googleapis.com/css2?family=Lato:wght@300;400&display=swap" rel="stylesheet">
<style>
  :root{
    --page:#ecebe6;
    --card:#ffffff;
    --brand:#c98a2e;
    --wave:#cfc83e;
    --accent:#ffc000;
    --icon:#c9c23a;
    --social:#a9d9c8;
    --text:#555555;
    --muted:#7a7a7a;
    --soft:#a8a8a8;
    --meadow-1:#f7f6ef;
    --meadow-2:#e3e8d3;
    --meadow-3:#d4dcc0;
  }
  *{margin:0;padding:0;box-sizing:border-box}
  html,body{width:1200px;height:900px;overflow:hidden}
  body{background:var(--page);font-family:"Lato",sans-serif;font-weight:300;color:var(--text);position:relative}
  .card{position:absolute;left:60px;top:142px;width:1080px;height:616px;background:var(--card);overflow:hidden;border:1px solid #dcdad2}
  .card-art{position:absolute;inset:0}
  .brand-name{position:absolute;left:56px;top:120px;font-size:58px;font-weight:300;color:var(--brand);line-height:1;letter-spacing:1px}
  .strapline{position:absolute;right:65px;top:118px;text-align:right;font-size:33px;line-height:41px;color:var(--muted)}
  .portrait{position:absolute;left:297px;top:358px;width:116px;height:116px;border-radius:50%;background:radial-gradient(circle at 50% 45%,#c9a58c,#6b5546)}
  .person{position:absolute;right:669px;top:490px;text-align:right;line-height:1}
  .person-name{font-size:42px;color:var(--text)}
  .person-title{font-size:30px;color:var(--soft);margin-top:8px}
  .contact{position:absolute;right:121px;text-align:right;line-height:1;font-size:33px;color:var(--text);white-space:nowrap}
  .contact.phone{font-size:36px;font-weight:400;top:336px}
  .contact.email{top:390px}
  .contact.web{top:462px}
  .contact.social{top:520px;right:194px}
  .icon{position:absolute;right:64px;width:34px;height:34px;border-radius:50%;background:var(--icon)}
  .icon svg{width:34px;height:34px;display:block}
  .icon.phone{top:348px}
  .icon.email{top:403px}
  .icon.web{top:475px}
  .social-dots{position:absolute;right:64px;top:530px;display:flex;gap:4px}
  .social-dots span{width:34px;height:34px;border-radius:50%;background:var(--social)}
</style>
</head>
<body>
<div class="card">
  <svg class="card-art" viewBox="0 0 1080 616" width="1080" height="616">
    <defs>
      <radialGradient id="meadow" cx="0.72" cy="0" r="0.9">
        <stop offset="0" stop-color="#fffdf6"/>
        <stop offset="0.35" stop-color="var(--meadow-1)"/>
        <stop offset="0.75" stop-color="var(--meadow-2)"/>
        <stop offset="1" stop-color="var(--meadow-3)"/>
      </radialGradient>
      <linearGradient id="rule" x1="0" x2="1">
        <stop offset="0" stop-color="#d8c53a"/>
        <stop offset="0.6" stop-color="var(--accent)"/>
        <stop offset="1" stop-color="#e39a35"/>
      </linearGradient>
    </defs>
    <path role="img" aria-label="Soft sunlit grass meadow backdrop"
      d="M0 0 H1080 V278 H470 C330 290 230 340 150 385 C110 405 95 405 88 390 C80 370 40 320 0 305 Z"
      fill="url(#meadow)"/>
    <path class="wave"
      d="M0 305 C40 320 80 370 88 390 C95 405 110 405 150 385 C230 340 330 290 470 278 C420 280 370 295 300 335 C220 380 150 436 90 438 C40 440 20 370 0 350 Z"
      fill="var(--wave)"/>
    <line x1="470" y1="278" x2="1080" y2="278" stroke="url(#rule)" stroke-width="4"/>
  </svg>

  <div class="brand-name">Tide Mentoring</div>

  <p class="strapline">A thinking<br>partner to help<br>you cut through the noise</p>

  <div class="portrait" role="img" aria-label="Portrait photo of Maren Delsby"></div>
  <div class="person">
    <div class="person-name">Maren Delsby</div>
    <div class="person-title">Business &amp; Personal Coach</div>
  </div>

  <div class="contact phone">+61 (0)438 915307</div>
  <div class="icon phone"><svg viewBox="0 0 34 34"><path d="M12 9 C10 9 9 11 9.5 13 C11 19 15 23 21 24.5 C23 25 25 24 25 22 L22 19 L19.5 20.5 C17 19.5 14.5 17 13.5 14.5 L15 12 Z" fill="#fff"/></svg></div>

  <div class="contact email">maren@tidementoring.com.au</div>
  <div class="icon email"><svg viewBox="0 0 34 34"><circle cx="17" cy="17" r="4" fill="none" stroke="#fff" stroke-width="2.2"/><path d="M21 14 V19 C21 21.5 25 21.5 25 17 A8 8 0 1 0 21 24" fill="none" stroke="#fff" stroke-width="2.2" stroke-linecap="round"/></svg></div>

  <div class="contact web">https://tidementoring.com.au</div>
  <div class="icon web"><svg viewBox="0 0 34 34"><g fill="none" stroke="#fff" stroke-width="2.2" stroke-linecap="round"><path d="M15 19 L19 15"/><path d="M16 12 L18 10 A3.5 3.5 0 0 1 24 15 L22 17"/><path d="M18 22 L16 24 A3.5 3.5 0 0 1 10 19 L12 17"/></g></svg></div>

  <div class="contact social">@tidementoringAU</div>
  <div class="social-dots" aria-hidden="true"><span></span><span></span><span></span></div>
</div>
</body>
</html>
```